A 3d printing services company "The Velvet Forge" needs a clutter breaking business card design

The Velvet Forge is a 3d design, animation and printing services company. We are in the B2B and B2C space. www.velvetforge.com.sg
We have been in business for a year.
The logo is already done (the current file is attached).
We need a business card design which reflects the 3d printing and animations services of the company. A standard rectangular shape is not an option. The card can be die cut.
The card should have the colors of the logo and should have a high tech wow feel to it.
The front of the card should have my name, designation, cellphone email and website details. No need for an office address.
Name: Ranjeet Kulkarni
Designation: Founder Director
Cellphone (65)91748253
email: ranjeet@velvetforge.com.sg
website: www.velvetforge.com.sg
The back of the card should have the services we offer:
1. 3d Design and Modelling
2. 3d Animation
3. 3D Printing
The tag line is: "make your ideas real"
Am uploading the current business card files(back and front).
Target Market(s)
Business owners and C level managers in Marine, Healthcare industry
Industry/Entity Type
Printing
Contact Information for Business Card
Name: Ranjeet Kulkarni
Cellphone (65)91748253
2. 3d Animation
3. 3D Printing
Look and feel

```html
<!DOCTYPE html>
<html lang="en">
<head>
<meta charset="utf-8">
<title>The Velvet Forge – Business Card</title>
<link rel="stylesheet" href="https://fonts.googleapis.com/css2?family=Exo+2:wght@400;500&display=swap">
<style>
  :root {
    --backdrop: #e9e6e1;
    --card-black: #0b0b0c;
    --band-dark: #1c1d1f;
    --band-light: #34363a;
    --accent-blue: #2f8fe6;
    --accent-deep: #2446c8;
    --bullet-blue: #3f9bf0;
    --text-white: #f2f2f2;
    --brand-green: #5fd12a;
  }
  html, body {
    margin: 0;
    padding: 0;
    width: 1200px;
    height: 1000px;
    overflow: hidden;
    background: var(--backdrop);
  }
  .canvas {
    display: block;
    width: 1200px;
    height: 1000px;
    font-family: "Exo 2", sans-serif;
  }
  .card-shape { fill: var(--card-black); }
  .texture-band { fill: url(#bandGradient); }
  .brand-well { fill: #070708; }
  .brand-mark { fill: var(--accent-deep); }
  .brand-name { fill: var(--brand-green); font-weight: 500; }
  .tagline { fill: var(--accent-blue); font-size: 31px; letter-spacing: 1.5px; }
  .bullet { fill: var(--bullet-blue); }
  .line-text { fill: var(--text-white); font-size: 21px; letter-spacing: 0.6px; }
  .website { fill: var(--accent-deep); font-size: 25px; letter-spacing: 0.8px; }
</style>
</head>
<body>
<svg class="canvas" viewBox="0 0 1200 1000" xmlns="http://www.w3.org/2000/svg">
  <defs>
    <linearGradient id="bandGradient" x1="0" y1="0" x2="0" y2="1">
      <stop offset="0" stop-color="var(--band-light)"/>
      <stop offset="1" stop-color="var(--band-dark)"/>
    </linearGradient>
    <clipPath id="backClip"><ellipse cx="545" cy="313" rx="455" ry="185"/></clipPath>
    <clipPath id="frontClip"><ellipse cx="775" cy="660" rx="355" ry="200"/></clipPath>
  </defs>

  <!-- Back of card: services -->
  <g class="card card-back">
    <ellipse class="card-shape" cx="545" cy="313" rx="455" ry="185"/>
    <g clip-path="url(#backClip)">
      <path class="texture-band" role="img" aria-label="Perforated metal texture band"
            d="M80 225 Q 545 150 1010 225 L 1010 300 Q 700 240 380 345 Q 220 390 80 395 Z"/>
    </g>
    <ellipse class="brand-well" cx="445" cy="282" rx="165" ry="80"/>
    <text class="tagline" x="480" y="168" text-anchor="middle">make your ideas real</text>
    <g class="brand">
      <circle class="brand-mark" cx="362" cy="282" r="30"/>
      <text class="brand-name" x="408" y="292" font-size="28">The Velvet Forge</text>
    </g>
    <g class="service-list">
      <circle class="bullet" cx="154" cy="388" r="5.5"/>
      <text class="line-text" x="170" y="396">3D Printing</text>
      <circle class="bullet" cx="207" cy="416" r="5.5"/>
      <text class="line-text" x="223" y="424">3d Animation</text>
      <circle class="bullet" cx="294" cy="444" r="5.5"/>
      <text class="line-text" x="310" y="452">3d Design and Modelling</text>
    </g>
  </g>

  <!-- Front of card: contact details -->
  <g class="card card-front">
    <ellipse class="card-shape" cx="775" cy="660" rx="355" ry="200"/>
    <g clip-path="url(#frontClip)">
      <path class="texture-band" role="img" aria-label="Perforated metal texture band"
            d="M420 560 Q 600 470 775 470 Q 950 470 1130 560 L 1130 610 Q 800 580 420 640 Z"/>
    </g>
    <ellipse class="brand-well" cx="770" cy="555" rx="105" ry="50"/>
    <g class="brand">
      <circle class="brand-mark" cx="706" cy="555" r="20"/>
      <text class="brand-name" x="734" y="562" font-size="19">The Velvet Forge</text>
    </g>
    <g class="contact-list">
      <circle class="bullet" cx="462" cy="653" r="5.5"/>
      <text class="line-text" x="478" y="662" font-size="22">Ranjeet Kulkarni</text>
      <circle class="bullet" cx="562" cy="685" r="5.5"/>
      <text class="line-text" x="578" y="693" style="font-size:19px">Founder Director</text>
      <circle class="bullet" cx="632" cy="716" r="5.5"/>
      <text class="line-text" x="650" y="725" style="font-size:22px">(65) 917 48 253</text>
      <circle class="bullet" cx="700" cy="746" r="5.5"/>
      <text class="line-text" x="717" y="754" style="font-size:20px">ranjeet@velvetforge.com.sg</text>
    </g>
    <text class="website" x="808" y="808" text-anchor="middle">www.velvetforge.com.sg</text>
  </g>
</svg>
</body>
</html>
```